Goal Planning Work Sheet

Design a better Goal Planning Worksheet that is fillable

Target Market(s)

People looking to make an important change

Industry/Entity Type

Work

Requirements
Must have
• Fillable pdf form
• Exceptional Design

```html
<!DOCTYPE html>
<html lang="en">
<head>
<meta charset="utf-8">
<title>Goal Planning Worksheet</title>
<link href="https://fonts.googleapis.com/css2?family=Roboto:wght@300;400;500;700&display=swap" rel="stylesheet">
<style>
  :root {
    --bg: #f3f3f3;
    --panel: #ffffff;
    --red: #d81e27;
    --cyan: #1cb3d3;
    --blue: #1b8ed0;
    --text: #727272;
    --label: #4f4f4f;
    --rule: #8a8a8a;
  }
  * { box-sizing: border-box; margin: 0; padding: 0; }
  html, body { width: 1200px; height: 900px; overflow: hidden; }
  body {
    background: var(--bg);
    font-family: "Roboto", Arial, sans-serif;
    font-weight: 300;
    color: var(--text);
    position: relative;
  }
  .masthead { position: absolute; left: 46px; top: 84px; display: flex; align-items: center; }
  .masthead-mark { width: 64px; height: 64px; border-radius: 50%; background: var(--red); margin-right: 26px; }
  .masthead-title {
    font-weight: 300; font-size: 68px; letter-spacing: -1px; line-height: 1;
    color: var(--cyan); white-space: nowrap;
  }

  .sidebar { position: absolute; width: 162px; }
  .sidebar-left { left: 53px; top: 182px; }
  .sidebar-right { left: 986px; top: 176px; }

  .section-head { display: flex; align-items: flex-start; margin-bottom: 6px; }
  .section-head svg { width: 16px; height: 36px; flex: none; margin-right: 12px; }
  .section-head h2 {
    color: var(--red); font-weight: 500; font-size: 18px; line-height: 20px;
    padding-top: 3px;
  }
  .key-list { list-style: none; }
  .key-list li {
    font-size: 12.6px; line-height: 20px; padding: 5px 0 4px;
    border-bottom: 1px solid var(--rule); white-space: nowrap;
  }
  .key-list li:first-child { padding-top: 0; }
  .key-list strong { color: var(--blue); font-weight: 700; }

  .fear { margin-top: 14px; }
  .fear .section-head { margin-bottom: 10px; }
  .fear .section-head h2 { padding-top: 9px; }

  .dare .section-head { margin-bottom: 10px; }
  .dare .section-head h2 { padding-top: 9px; }
  .dare .key-list li { padding: 6px 0 8px; }
  .dare .key-list li:first-child { padding-top: 0; }
  .process { margin-top: 34px; }
  .process .section-head { margin-bottom: 4px; }
  .step-list { list-style: none; }
  .step-list li {
    display: flex; align-items: center; font-size: 12.6px; line-height: 20px;
    padding: 5px 0 4px; border-bottom: 1px solid var(--rule);
  }
  .step-list svg { width: 22px; height: 20px; flex: none; margin-right: 12px; fill: var(--blue); }

  .panel {
    position: absolute; background: var(--panel); border-radius: 6px;
    padding: 14px 10px 0;
  }
  .panel-label {
    font-size: 12.6px; line-height: 20px; color: var(--text);
    border-bottom: 1px solid var(--rule); padding-bottom: 7px; white-space: nowrap;
  }
  .panel-label strong { color: var(--label); font-weight: 700; }
  .panel textarea {
    display: block; width: 100%; border: 0; resize: none; background: transparent;
    font: 300 13px/20px "Roboto", Arial, sans-serif; color: var(--label);
    margin-top: 8px; outline: none;
  }
  .panel-imagine { left: 240px; top: 170px; width: 360px; height: 220px; }
  .panel-roadblocks { left: 240px; top: 400px; width: 360px; height: 220px; padding-top: 20px; }
  .panel-team { left: 240px; top: 630px; width: 360px; height: 220px; }
  .panel-specific { left: 614px; top: 170px; width: 346px; height: 450px; }
  .panel-evaluate { left: 614px; top: 630px; width: 346px; height: 220px; }
  .panel-imagine .panel-label, .panel-roadblocks .panel-label { margin-right: 13px; }
</style>
</head>
<body>
  <header class="masthead">
    <div class="masthead-mark" aria-hidden="true"></div>
    <h1 class="masthead-title">I’M MOVING FORWARD NOW</h1>
  </header>

  <aside class="sidebar sidebar-left">
    <section class="strengths">
      <div class="section-head">
        <svg viewBox="0 0 16 36"><path d="M3 2 L13 18 L3 34" fill="none" stroke="#1b8ed0" stroke-width="3.5" stroke-linejoin="round"/></svg>
        <h2>STRENGTH<br>SPOTTING</h2>
      </div>
      <ul class="key-list">
        <li><strong>Wisdom:</strong> Cognitive<br>Creativity Curiosity Judgment<br>Love of Learning Perspective</li>
        <li><strong>Courage:</strong> Bravery<br>Perseverance Honesty Zest</li>
        <li><strong>Humanity:</strong> Love Kindness<br>Social Intelligence Teamwork</li>
        <li><strong>Justice:</strong> Fairness Leadership</li>
        <li><strong>Temperance:</strong> Forgiveness<br>Humility Prudence Self-<br>Regulation</li>
        <li><strong>Transcendence</strong>:<br>Appreciation Beauty &amp;<br>Excellence Gratitude Hope<br>Humor Spirituality</li>
      </ul>
    </section>
    <section class="fear">
      <div class="section-head">
        <svg viewBox="0 0 16 36"><path d="M3 2 L13 18 L3 34" fill="none" stroke="#1b8ed0" stroke-width="3.5" stroke-linejoin="round"/></svg>
        <h2>F.E.A.R</h2>
      </div>
      <ul class="key-list">
        <li><strong>Fuse</strong> To Thoughts and<br>Feelings</li>
        <li><strong>Excessive</strong> Thinking</li>
        <li><strong>Attractors</strong> Negative<br>Emotional</li>
        <li><strong>Run</strong> Away &amp; Avoidance</li>
      </ul>
    </section>
  </aside>

  <section class="panel panel-imagine">
    <p class="panel-label"><strong>Imagine and Move</strong> (motion creates emotion)<br>Being the person I want to be, Values, Character Strengths:</p>
    <textarea rows="7" aria-label="Imagine and Move"></textarea>
  </section>
  <section class="panel panel-roadblocks">
    <p class="panel-label"><strong>Roadblocks</strong> Resources Rewards Ramification:</p>
    <textarea rows="7" aria-label="Roadblocks"></textarea>
  </section>
  <section class="panel panel-team">
    <p class="panel-label"><strong>Team Roles:</strong></p>
    <textarea rows="7" aria-label="Team Roles"></textarea>
  </section>
  <section class="panel panel-specific">
    <p class="panel-label"><strong>Specific</strong> Small Meaningful Measurable Actionable<br>Attainable Timeline Now:</p>
    <textarea rows="18" aria-label="Specific goal"></textarea>
  </section>
  <section class="panel panel-evaluate">
    <p class="panel-label"><strong>Evaluate,</strong> Emotions, Revise, Resilient</p>
    <textarea rows="7" aria-label="Evaluate"></textarea>
  </section>

  <aside class="sidebar sidebar-right">
    <section class="dare">
      <div class="section-head">
        <svg viewBox="0 0 16 36"><path d="M3 2 L13 18 L3 34" fill="none" stroke="#1b8ed0" stroke-width="3.5" stroke-linejoin="round"/></svg>
        <h2>D.A.R.E</h2>
      </div>
      <ul class="key-list">
        <li><strong>Defuse:</strong> Notice, Name,<br>Normalize</li>
        <li><strong>Acceptance:</strong> Allow,<br>Appreciate</li>
        <li><strong>Reinforce</strong> Skills &amp; Support</li>
        <li><strong>Enjoy</strong> Values</li>
      </ul>
    </section>
    <section class="process">
      <div class="section-head">
        <svg viewBox="0 0 16 36"><path d="M3 2 L13 18 L3 34" fill="none" stroke="#1b8ed0" stroke-width="3.5" stroke-linejoin="round"/></svg>
        <h2>PROBLEM<br>SOLVING<br>PROCESS</h2>
      </div>
      <ul class="step-list">
        <li><svg viewBox="0 0 22 20"><path d="M1 3 L7 1 L14 3 L21 1 V17 L14 19 L7 17 L1 19 Z"/></svg>Domain of Problem</li>
        <li><svg viewBox="0 0 22 20"><circle cx="5" cy="5" r="3"/><circle cx="11" cy="4" r="3"/><circle cx="17" cy="5" r="3"/><rect x="2" y="9" width="6" height="10" rx="2"/><rect x="8" y="8" width="6" height="11" rx="2"/><rect x="14" y="9" width="6" height="10" rx="2"/></svg>Team Gathered</li>
        <li><svg viewBox="0 0 22 20"><path d="M1 14 Q8 10 13 13 L20 11 L21 14 L12 18 L1 17 Z"/><circle cx="10" cy="4" r="1.5"/><circle cx="15" cy="3" r="1.5"/><circle cx="13" cy="8" r="1.5"/><circle cx="18" cy="7" r="1.5"/></svg>Values Focus</li>
        <li><svg viewBox="0 0 22 20"><path d="M5 14 A4 4 0 0 1 5 6 A6 6 0 0 1 16 5 A4.5 4.5 0 0 1 17 14 Z"/><circle cx="6" cy="17" r="1.5"/></svg>Imagine, Move, Be</li>
        <li><svg viewBox="0 0 22 20"><path d="M4 6 H8 A2.5 2.5 0 1 1 13 6 H17 V10 A2.5 2.5 0 1 1 17 15 V19 H4 Z" transform="rotate(-15 11 11)"/></svg>Define Problem,<br>Cause, Solutions</li>
        <li><svg viewBox="0 0 22 20"><rect x="2" y="1" width="18" height="18" rx="3"/><rect x="6" y="5" width="11" height="1.6" fill="#fff"/><rect x="6" y="9" width="11" height="1.6" fill="#fff"/><rect x="6" y="13" width="11" height="1.6" fill="#fff"/></svg>Plan-SMARTER Goals</li>
        <li><svg viewBox="0 0 22 20"><rect x="5" y="1" width="15" height="4"/><rect x="5" y="6" width="15" height="4"/><rect x="5" y="11" width="15" height="4"/><path d="M1 12 H5 L9 16 H20 V19 H1 Z"/></svg>Resources &amp;<br>Resourcefulness</li>
        <li><svg viewBox="0 0 22 20"><path d="M8 1 H14 L18 19 H4 Z" fill="none" stroke="#1b8ed0" stroke-width="2"/><path d="M11 15 L17 3" stroke="#1b8ed0" stroke-width="2"/></svg>Practice, Rehearse</li>
        <li><svg viewBox="0 0 22 20"><path d="M20 1 C13 1 8 6 6 12 L9 15 C15 13 20 8 20 1 Z"/><path d="M6 12 L2 11 L6 7 Z"/><path d="M9 15 L10 19 L13 14 Z"/><path d="M5 15 L2 19 L6 17 Z"/></svg>Act Communicate</li>
        <li><svg viewBox="0 0 22 20"><path d="M11 2 V18 M4 5 H18 M7 18 H15" stroke="#1b8ed0" stroke-width="1.6" fill="none"/><path d="M1 12 L4 5 L7 12 Z M15 12 L18 5 L21 12 Z"/></svg>Evaluate Revise</li>
      </ul>
    </section>
  </aside>
</body>
</html>
```